Hawaiian Body Care Product Catalog for Wholesaling

Design a multi page catalog for a Hawaiian body care brand. There are about 6 different types of products (for example, soaps, lotions, lip balms) and we have about 50 products.

Catalog size: 5.5" x 8.5"

Please visit our website at www.corallumecare.example to get an idea of our product line and aesthetic. We would like to focus on the fun tropical fruit. This catalog to for sales reps to show retailers - so it's a wholesale catalog.

Target Market(s)

Retailers as were are wholesaling to them.

Industry/Entity Type

Beauty

Font styles to use
Sans Serif

Colors

Designer to choose colors to be used in the design.

Requirements
Must have
• Images of tropical fruit - we have a lot of stock images that I was unable to file transfer because it said they were too wide.
• Hi Res images for print.
Nice to have
• Images of each product per type of product. Descriptions of the products found on website. SKU under the images of each product. no pricing, just sku number. Playful images of tropical fruit, flowers and Hawaii. Somewhere we need to explain that we are donating 5% net profits to protect Hawaiian Wildlife, so maybe a page dedicated to that with an image of Hawaiian Wildlife.

```html
<!DOCTYPE html>
<html lang="en">
<head>
<meta charset="UTF-8">
<title>Corallume Product Catalog</title>
<link href="https://fonts.googleapis.com/css2?family=Montserrat:wght@400;600;700;800&display=swap" rel="stylesheet">
<style>
  :root {
    --bg: #cfe5e6;
    --yellow: #f7dc4a;
    --yellow-deep: #f2c82c;
    --pink: #ec4f8c;
    --coral: #f6806f;
    --blue: #3f8fd8;
    --teal-panel: #2f6d86;
    --leaf: #4f9a48;
    --paper: #ffffff;
    --ink: #3a3a3a;
    --muted: #8a8a8a;
  }
  * { box-sizing: border-box; margin: 0; padding: 0; }
  html, body { width: 720px; height: 1200px; overflow: hidden; }
  body {
    background: var(--bg);
    font-family: "Montserrat", sans-serif;
    color: var(--ink);
    display: flex;
    flex-direction: column;
    align-items: center;
    gap: 40px;
    padding-top: 40px;
  }

  /* Cover */
  .cover {
    position: relative;
    width: 560px;
    height: 340px;
    background: var(--yellow);
    overflow: hidden;
  }
  .cover-fruit {
    position: absolute;
    top: 0; right: 0;
    width: 330px; height: 190px;
    background: radial-gradient(circle at 30% 40%, #f08aa6 0 18%, transparent 19%),
                radial-gradient(circle at 70% 55%, #f47b5e 0 20%, transparent 21%),
                radial-gradient(circle at 50% 80%, #9fd26a 0 9%, transparent 10%),
                linear-gradient(135deg, var(--yellow-deep), #f5a36a);
    border-bottom-left-radius: 120px;
  }
  .cover-brand {
    position: absolute;
    left: 40px; top: 178px;
    font-weight: 700;
    font-size: 40px;
    color: var(--paper);
    letter-spacing: 1px;
  }
  .cover-title {
    position: absolute;
    left: 42px; top: 232px;
    font-weight: 800;
    font-size: 15px;
    letter-spacing: 3px;
    color: var(--pink);
  }
  .cover-band {
    position: absolute;
    left: 40px; top: 258px;
    background: var(--pink);
    color: var(--paper);
    font-size: 8px;
    font-weight: 600;
    letter-spacing: 1.5px;
    padding: 4px 14px;
    text-transform: uppercase;
  }

  /* Spreads */
  .spread {
    width: 640px;
    height: 340px;
    display: flex;
    background: var(--paper);
    box-shadow: 0 2px 0 rgba(0,0,0,0.05);
  }
  .page {
    position: relative;
    width: 50%;
    height: 100%;
    overflow: hidden;
  }
  .page + .page { border-left: 1px solid #e6e6e6; }

  .photo { position: absolute; }
  .leaf-edge {
    left: 0; top: 50px; width: 90px; height: 230px;
    background: linear-gradient(160deg, #f6a05a, var(--leaf) 55%, #2e7a3a);
    border-radius: 0 120px 120px 0;
  }
  .tag {
    display: inline-block;
    background: var(--pink);
    color: var(--paper);
    font-size: 8px;
    font-weight: 700;
    letter-spacing: 1px;
    padding: 3px 10px;
    text-transform: uppercase;
  }
  .intro {
    position: absolute;
    left: 110px; top: 40px; width: 190px;
  }
  .intro p { font-size: 8px; color: var(--muted); margin-top: 8px; line-height: 1.5; }

  .product { display: flex; flex-direction: column; align-items: center; gap: 4px; }
  .product-shot { width: 34px; height: 46px; border-radius: 4px; }
  .product-name { font-size: 7px; font-weight: 600; color: var(--ink); }
  .sku {
    font-size: 6px; font-weight: 700; color: var(--paper);
    background: var(--blue); padding: 2px 8px; border-radius: 2px;
  }
  .shot-pink { background: linear-gradient(#f9c1d5, var(--pink)); }
  .shot-yellow { background: linear-gradient(#fff1a8, var(--yellow-deep)); }
  .shot-coral { background: linear-gradient(#ffd0c4, var(--coral)); }
  .shot-green { background: linear-gradient(#d6efc2, var(--leaf)); }

  .left-products {
    position: absolute; left: 120px; top: 110px;
    display: grid; grid-template-columns: repeat(2, 80px); gap: 16px 20px;
  }
  .grid-products {
    position: absolute; left: 30px; top: 40px; right: 30px;
    display: grid; grid-template-columns: repeat(3, 1fr); gap: 22px 10px;
  }

  .fruit-spread {
    left: 0; top: 0; width: 100%; height: 100%;
    background: radial-gradient(circle at 60% 45%, #f2d36a 0 22%, transparent 23%),
                radial-gradient(circle at 30% 75%, #8fbf4f 0 14%, transparent 15%),
                linear-gradient(135deg, #eef3e4, #d9ead0);
  }
  .giving {
    position: absolute; right: 16px; top: 40px;
    width: 110px; height: 250px;
    background: var(--teal-panel);
    color: var(--paper);
    padding: 18px 12px;
  }
  .giving h2 { font-size: 11px; font-weight: 800; letter-spacing: 1px; text-transform: uppercase; }
  .giving p { font-size: 7.5px; line-height: 1.6; margin-top: 10px; }
  .fruit-corner {
    right: 0; bottom: 0; width: 80px; height: 110px;
    background: linear-gradient(160deg, #f08aa6, #9fd26a);
    border-top-left-radius: 80px;
  }
  .note {
    position: absolute; left: 30px; bottom: 34px;
    border: 1px solid var(--pink);
    color: var(--pink);
    font-size: 7px; font-weight: 600;
    padding: 6px 10px;
  }
</style>
</head>
<body>

  <section class="cover">
    <div class="cover-fruit" role="img" aria-label="Sliced papaya, grapefruit, dragon fruit and limes on a yellow backdrop"></div>
    <div class="cover-brand">corallume</div>
    <div class="cover-title">PRODUCT CATALOG</div>
    <div class="cover-band">Wholesale Collection 2024</div>
  </section>

  <section class="spread">
    <div class="page">
      <div class="photo leaf-edge" role="img" aria-label="Tropical leaves with grapefruit and citrus slices"></div>
      <div class="intro">
        <span class="tag">Body Soaps</span>
        <p>Handmade with tropical fruit oils.</p>
      </div>
      <div class="left-products">
        <div class="product"><div class="product-shot shot-pink" role="img" aria-label="Soap bar product photo"></div><span class="product-name">Papaya Bar</span><span class="sku">SKU 101</span></div>
        <div class="product"><div class="product-shot shot-coral" role="img" aria-label="Soap bar product photo"></div><span class="product-name">Guava Bar</span><span class="sku">SKU 102</span></div>
        <div class="product"><div class="product-shot shot-yellow" role="img" aria-label="Soap bar product photo"></div><span class="product-name">Mango Bar</span><span class="sku">SKU 103</span></div>
      </div>
    </div>
    <div class="page">
      <div class="grid-products">
        <div class="product"><div class="product-shot shot-pink" role="img" aria-label="Lotion bottle product photo"></div><span class="product-name">Guava Lotion</span><span class="sku">SKU 201</span></div>
        <div class="product"><div class="product-shot shot-yellow" role="img" aria-label="Lotion bottle product photo"></div><span class="product-name">Mango Lotion</span><span class="sku">SKU 202</span></div>
        <div class="product"><div class="product-shot shot-coral" role="img" aria-label="Lotion bottle product photo"></div><span class="product-name">Papaya Lotion</span><span class="sku">SKU 203</span></div>
        <div class="product"><div class="product-shot shot-green" role="img" aria-label="Body oil bottle product photo"></div><span class="product-name">Lime Oil</span><span class="sku">SKU 204</span></div>
        <div class="product"><div class="product-shot shot-pink" role="img" aria-label="Body oil bottle product photo"></div><span class="product-name">Lychee Oil</span><span class="sku">SKU 205</span></div>
        <div class="product"><div class="product-shot shot-yellow" role="img" aria-label="Body oil bottle product photo"></div><span class="product-name">Pineapple Oil</span><span class="sku">SKU 206</span></div>
      </div>
    </div>
  </section>

  <section class="spread">
    <div class="page">
      <div class="photo fruit-spread" role="img" aria-label="Pineapple, avocado, lemons and palm leaves on white"></div>
      <div class="giving">
        <h2>Giving Back</h2>
        <p>We donate five percent of net profits to protect Hawaiian wildlife.</p>
      </div>
    </div>
    <div class="page">
      <div class="grid-products">
        <div class="product"><div class="product-shot shot-coral" role="img" aria-label="Lip balm product photo"></div><span class="product-name">Coconut Balm</span><span class="sku">SKU 301</span></div>
        <div class="product"><div class="product-shot shot-pink" role="img" aria-label="Lip balm product photo"></div><span class="product-name">Guava Balm</span><span class="sku">SKU 302</span></div>
        <div class="product"><div class="product-shot shot-yellow" role="img" aria-label="Lip balm product photo"></div><span class="product-name">Mango Balm</span><span class="sku">SKU 303</span></div>
        <div class="product"><div class="product-shot shot-green" role="img" aria-label="Body scrub jar product photo"></div><span class="product-name">Lime Scrub</span><span class="sku">SKU 304</span></div>
        <div class="product"><div class="product-shot shot-coral" role="img" aria-label="Body scrub jar product photo"></div><span class="product-name">Papaya Scrub</span><span class="sku">SKU 305</span></div>
        <div class="product"><div class="product-shot shot-pink" role="img" aria-label="Body scrub jar product photo"></div><span class="product-name">Lychee Scrub</span><span class="sku">SKU 306</span></div>
      </div>
      <div class="note">Ask your rep about display kits.</div>
      <div class="photo fruit-corner" role="img" aria-label="Pineapple and grapes at the page corner"></div>
    </div>
  </section>

</body>
</html>
```